Pumpkin Seed Oil Dark Green Plastic Bottle Needs a Label Design

We need a label design for an Slovenian tourist farm from an agricultural area called Prekmurje and known for its gourmet delicacies.

We would like to be presented with label designs for a 1 litre (approximately 33.814 U.S. fluid ounces) dark green plastic bottle containing undiluted (ie. 100%), viscous and very dark green (almost black) pumpkin seed oil. The label design should be consistent with nature and food processing industry, represent adequate colours, be 11 centimetres (approximately 4.331 inches) high and 7.5 centimetres (approximately 2.953 inches) wide and have enough blank/empty space (approximately 1/3 of the label) for the subsequently added legally stipulated text.

We look forward to receive visual and appealing label designs that ought to communicate quality, trust and, most importantly, the geographical indication/location/origin.

We would like to add that the said client has not yet worked on their corporate identity (colours, fonts ...) which means that ample freedom is allowed and should be taken advantage of.
Updates

Project Deadline Extended
Reason: We received merely 6 label designs while we expected to receive quite a few more. The provided task description remains the same.

Target Market(s)

Wider public and (small) retailers.

Industry/Entity Type

Agribusiness

Requirements
Must have
• Label design size: 11 centimetres (approximately 4.331 inches) x 7.5 centimetres (approximately 2.953 inches).
• Blank/empty space: approximately 1/3 of the label.
Nice to have
• Be visual.
• Communicate quality, trust and, most importantly, the geographical indication/location/origin.

```html
<!DOCTYPE html>
<html lang="en">
<head>
<meta charset="utf-8">
<title>Natural Pumpkin Seed Oil Label</title>
<link href="https://fonts.googleapis.com/css2?family=Bebas+Neue&family=Crimson+Text:wght@400;600&display=swap" rel="stylesheet">
<style>
  :root {
    --page: #ffffff;
    --label-bg: #ead3ac;
    --frame: #f0873f;
    --band: #a05340;
    --gold: #ffc60b;
    --forest: #4b5a27;
    --rust-text: #9e523f;
    --ink: #231f20;
  }
  * { margin: 0; padding: 0; box-sizing: border-box; }
  html, body {
    width: 866px; height: 1200px; overflow: hidden;
    background: var(--page);
  }
  .canvas { position: relative; width: 866px; height: 1200px; }
  .label {
    position: absolute; left: 107px; top: 121px;
    width: 667px; height: 977px;
    background: var(--label-bg);
  }
  .frame {
    position: absolute; left: 32px; top: 31px;
    width: 607px; height: 906px;
    border: 2px solid var(--frame);
    border-radius: 64px;
  }
  .brand {
    position: absolute; left: 50%; top: 40px;
    transform: translateX(-50%);
    display: flex; align-items: center; gap: 12px;
    padding: 0 18px;
    background: var(--label-bg);
    font-family: "Crimson Text", serif;
    font-weight: 600; font-size: 34px;
    color: var(--forest);
    white-space: nowrap;
  }
  .brand-dot {
    width: 22px; height: 22px; border-radius: 50%;
    background: var(--forest);
  }
  .serif { font-family: "Crimson Text", serif; text-align: center; position: absolute; left: 0; width: 100%; line-height: 1; }
  .natural { top: 174px; font-size: 48px; color: var(--rust-text); }
  .title-band {
    position: absolute; left: 30px; top: 237px;
    width: 611px; height: 205px;
    background: var(--band);
    font-family: "Bebas Neue", sans-serif;
    font-weight: 400;
    color: var(--gold);
    overflow: hidden;
  }
  .title-band .line {
    position: absolute; left: 0; width: 100%;
    text-align: center;
    font-size: 108px; line-height: 1;
    letter-spacing: 1px;
    white-space: nowrap;
  }
  .title-band .line-top { top: 9px; }
  .title-band .line-bottom { top: 105px; word-spacing: -10px; }
  .qualifier { top: 470px; font-size: 25px; color: var(--ink); }
  .method { top: 506px; font-size: 62px; color: var(--ink); }
  .organic { top: 579px; font-size: 28px; color: var(--ink); }
  .illustration {
    position: absolute; left: 48px; top: 619px;
    width: 401px; height: 280px;
    border-radius: 140px 140px 40px 40px;
    background: radial-gradient(circle at 48% 62%, #f7a91c 0%, #f39a1a 28%, #6d9a3a 52%, rgba(94,140,50,0.5) 72%, rgba(234,211,172,0) 100%);
  }
  .volume {
    position: absolute; left: 241px; top: 915px;
    width: 186px; height: 44px;
    border: 2px solid var(--forest);
    border-radius: 22px;
    background: var(--gold);
    font-family: "Crimson Text", serif;
    font-size: 29px; color: var(--ink);
    display: flex; align-items: center; justify-content: center;
    gap: 14px; line-height: 1;
  }
</style>
</head>
<body>
<div class="canvas">
  <div class="label">
    <div class="frame"></div>
    <div class="brand"><span class="brand-dot"></span>Mura Valley Farm</div>
    <p class="serif natural">Natural</p>
    <h1 class="title-band">
      <span class="line line-top">PUMPKIN</span>
      <span class="line line-bottom">SEED OIL</span>
    </h1>
    <p class="serif qualifier">undiluted &amp; unrefind</p>
    <p class="serif method">Cold Pressed</p>
    <p class="serif organic">100% Organic</p>
    <div class="illustration" role="img" aria-label="Illustration of an orange pumpkin with green vines, leaves and curling tendrils"></div>
    <div class="volume"><span>1l</span><span>33.814 oz</span></div>
  </div>
</div>
</body>
</html>
```